Business Card Design

We have recently seen two business cards that caught our attention and think the designs would work for us. We are an accounting firm that serves small businesses in a variety of industries. Attached are the two business card that inspired us along with very rough layouts. We would like to see a professional layout using our company information.

Industry/Entity Type

Accounting

Contact Information for Business Card

Company Name - Porter Lyle
Address - 4120 Marbury Lane, Suite 310, Houston, TX 77058
713-555-0186 - Main
281-555-0143 - Fax

Team Member Names, emails and phone numbers (see attachment)

```html
<!DOCTYPE html>
<html lang="en">
<head>
<meta charset="utf-8">
<title>Porter Lyle Business Cards</title>
<link rel="stylesheet" href="https://fonts.googleapis.com/css2?family=Lato:wght@400;700&display=swap">
<style>
  :root {
    --paper: #ffffff;
    --ink: #1e1e1e;
    --ink-soft: #3a3a3a;
    --mark: #3d3d3f;
    --rule: #8a8a8a;
    --frame: #222222;
  }
  * { box-sizing: border-box; margin: 0; padding: 0; }
  html, body { width: 1200px; height: 1088px; overflow: hidden; background: var(--paper); }
  body { position: relative; font-family: "Lato", Arial, sans-serif; color: var(--ink); }

  .card {
    position: absolute;
    width: 488px;
    height: 279px;
    background: var(--paper);
    border: 1.5px solid var(--frame);
  }
  .card--top-left     { left: 95px;  top: 108px; }
  .card--top-right    { left: 608px; top: 112px; }
  .card--bottom-left  { left: 96px;  top: 413px; }
  .card--bottom-right { left: 609px; top: 413px; }
  .card--back         { left: 319px; top: 745px; height: 280px; }

  .identity {
    position: absolute;
    left: 18px;
    width: 190px;
    top: 0;
    text-align: center;
  }
  .identity__brand {
    margin-top: 100px;
    height: 44px;
    font-size: 25px;
    font-weight: 700;
    color: var(--mark);
    letter-spacing: 0.5px;
    line-height: 44px;
  }
  .identity__name {
    margin-top: 28px;
    font-size: 15px;
    text-transform: uppercase;
    letter-spacing: 0.2px;
    line-height: 18px;
  }
  .identity__title {
    font-size: 11.5px;
    line-height: 16px;
  }

  .divider {
    position: absolute;
    left: 231px;
    top: 49px;
    width: 1px;
    height: 170px;
    background: var(--rule);
  }

  .details {
    position: absolute;
    left: 256px;
    top: 58px;
    font-size: 12px;
    line-height: 15.5px;
    color: var(--ink-soft);
  }
  .phones { margin-top: 13px; border-collapse: collapse; }
  .phones td { padding: 0; line-height: 16px; }
  .phones .phones__label { width: 44px; }
  .details__email { margin-top: 12px; }

  .back-brand {
    position: absolute;
    inset: 0;
    display: flex;
    align-items: center;
    justify-content: center;
    gap: 18px;
    font-size: 52px;
    font-weight: 700;
    color: var(--mark);
    letter-spacing: 1px;
  }
  .back-brand__square {
    width: 22px;
    height: 22px;
    background: var(--mark);
  }
</style>
</head>
<body>

<section class="card card--top-left">
  <div class="identity">
    <div class="identity__brand">Porter Lyle</div>
    <div class="identity__name">Marisa Dalton</div>
    <div class="identity__title">Account Manager</div>
  </div>
  <div class="divider"></div>
  <div class="details">
    <div class="details__company">Porter Lyle Enterprises, LLC</div>
    <div>4120 Marbury Lane, Suite 310</div>
    <div>Houston, TX 77058</div>
    <table class="phones">
      <tr><td class="phones__label">Mobile</td><td>832-555-0117</td></tr>
      <tr><td class="phones__label">Direct</td><td>713-555-0122</td></tr>
      <tr><td class="phones__label">Main</td><td>713-555-0186</td></tr>
      <tr><td class="phones__label">Fax</td><td>281-555-0143</td></tr>
    </table>
    <div class="details__email">mdalton@porterlyle.com</div>
  </div>
</section>

<section class="card card--top-right">
  <div class="identity">
    <div class="identity__brand">Porter Lyle</div>
    <div class="identity__name">Colleen Rae Whitford</div>
    <div class="identity__title">Account Manager</div>
  </div>
  <div class="divider"></div>
  <div class="details">
    <div class="details__company">Porter Lyle Enterprises, LLC</div>
    <div>4120 Marbury Lane, Suite 310</div>
    <div>Houston, TX 77058</div>
    <table class="phones">
      <tr><td class="phones__label">Mobile</td><td>713-555-0139</td></tr>
      <tr><td class="phones__label">Direct</td><td>713-555-0121</td></tr>
      <tr><td class="phones__label">Main</td><td>713-555-0186</td></tr>
      <tr><td class="phones__label">Fax</td><td>281-555-0143</td></tr>
    </table>
    <div class="details__email">CRae@porterlyle.com</div>
  </div>
</section>

<section class="card card--bottom-left">
  <div class="identity">
    <div class="identity__brand">Porter Lyle</div>
    <div class="identity__name">Helen J. Barlow</div>
    <div class="identity__title">Office Manager</div>
  </div>
  <div class="divider"></div>
  <div class="details">
    <div class="details__company">Porter Lyle Enterprises, LLC</div>
    <div>4120 Marbury Lane, Suite 310</div>
    <div>Houston, TX 77058</div>
    <table class="phones">
      <tr><td class="phones__label">Mobile</td><td>832-555-0164</td></tr>
      <tr><td class="phones__label">Direct</td><td>713-555-0100</td></tr>
      <tr><td class="phones__label">Main</td><td>713-555-0186</td></tr>
      <tr><td class="phones__label">Fax</td><td>281-555-0143</td></tr>
    </table>
    <div class="details__email">hbarlow@porterlyle.com</div>
  </div>
</section>

<section class="card card--bottom-right">
  <div class="identity">
    <div class="identity__brand">Porter Lyle</div>
    <div class="identity__name">Ruth A. Lyle</div>
    <div class="identity__title">President</div>
  </div>
  <div class="divider"></div>
  <div class="details">
    <div class="details__company">Porter Lyle Enterprises, LLC</div>
    <div>4120 Marbury Lane, Suite 310</div>
    <div>Houston, TX 77058</div>
    <table class="phones">
      <tr><td class="phones__label">Mobile</td><td>281-555-0178</td></tr>
      <tr><td class="phones__label">Direct</td><td>713-555-0123</td></tr>
      <tr><td class="phones__label">Main</td><td>713-555-0186</td></tr>
      <tr><td class="phones__label">Fax</td><td>281-555-0143</td></tr>
    </table>
    <div class="details__email">ralyle@porterlyle.com</div>
  </div>
</section>

<section class="card card--back">
  <div class="back-brand">
    <span class="back-brand__square"></span>
    <span class="back-brand__name">Porter Lyle</span>
  </div>
</section>

</body>
</html>
```